Korlane Email Signature Banners – Fabrication Capability Series

www.Korlane.com.au is an Australian engineering and fabrication company specialising in fabrication and welding of :
steel piping spools,
skids and frames,
small volume process steel tanks
and general steel fabrication
We require four distinct banner designs for use in Velnor Tidmark email signatures. Each banner will highlight a specific capability while maintaining a consistent brand identity.
Deliverables
Four banners total:
Piping Spools Fabrication – focus on precision welding and stainless steel pipework
Skid & Frames Fabrication – highlight skid systems and structural frames
Small Steel Tanks Fabrication – show fabricated tanks and workshop craftsmanship
General Fabrication Solutions – broad steel fabrication theme for company-wide use
Dimensions: 600–700 px wide × 100 px high
Format: PNG (preferred), small file size prefered
Resolution: 72 dpi
Background: non-transparent, industrial or workshop setting
Text examples:
1. Piping Spools Fabrication
Option A: “Expert Fabrication Solutions for Process Piping”
Option B: “Precision Welding for Complex Systems”
Option C: “Delivering Quality in Every Spool”
Option D: “Engineered for Flow, Built for Strength”
2. Skid & Frames Fabrication
Option A: “Custom Engineered Modular Systems”
Option B: “Built Strong. Designed Smart.”
Option C: “Reliable Frames for Industrial Performance”
Option D: “Modular Fabrication for Seamless Integration”
3. Small Steel Tanks Fabrication
Option A: “Precision Built for Your Needs”
Option B: “Compact Strength. Proven Durability.”
Option C: “Fabricated for Performance and Longevity”
Option D: “Small Tanks. Big Reliability.”
4. General Fabrication Solutions
Option A: “Quality Craftsmanship, Proven Results”
Option B: “Your Partner in Precision Fabrication”
Option C: “Engineering Excellence in Every Weld”
Option D: “Australian Fabrication. Global Standards.”
Style Direction
Clean, professional, and engineering‑focused
Use Korlane brand colours
Blend photo realism with vector clarity (no heavy gradients)
Include subtle industrial textures or workshop imagery
Typography: bold sans‑serif, legible at small scale
Usage Context
These banners will appear at the bottom of staff email signatures via Tidmark Email Signature Tool for Velnor 365, so clarity and fast loading are essential. No Logo is required in the banners.
Reference
Existing Korlane signature is attached. Colour palette to match the signature style and logo.
Target Market(s)
Engineering and construction companies,
Industry/Entity Type
Engineering fabrication design
Look and feel

```html
<!DOCTYPE html>
<html lang="en">
<head>
<meta charset="UTF-8">
<title>Korlane Email Signature Banners</title>
<link rel="stylesheet" href="https://fonts.googleapis.com/css2?family=Oswald:wght@600&family=Roboto:wght@400;500&display=swap">
<style>
  :root {
    --board-light: #d2d2d2;
    --board-dark: #a9a9a9;
    --navy: #1b3d78;
    --navy-deep: #142f60;
    --brand-blue: #0b6db5;
    --brand-blue-light: #1d8fd6;
    --sky: #45b8ea;
    --sky-soft: #3aa6dc;
    --white: #ffffff;
    --steel: #6f86a6;
    --steel-dark: #3a4f70;
  }
  * { margin: 0; padding: 0; box-sizing: border-box; }
  html, body { width: 1200px; height: 717px; overflow: hidden; }
  body {
    background: radial-gradient(ellipse at 50% 45%, var(--board-light) 0%, var(--board-dark) 100%);
    position: relative;
    font-family: "Roboto", Arial, sans-serif;
  }
  .banner {
    position: absolute;
    left: 89px;
    width: 1022px;
    height: 146px;
    overflow: hidden;
    box-shadow: 0 6px 18px rgba(0,0,0,0.25);
  }
  .banner--spools { top: 108px; background: linear-gradient(90deg, var(--brand-blue) 0%, var(--brand-blue-light) 45%, var(--brand-blue) 100%); }
  .banner--skids { top: 286px; background: var(--navy); }
  .banner--tanks { top: 464px; background: var(--navy); }

  .photo { position: absolute; top: 0; height: 100%; }
  .banner--spools .photo {
    right: 0; width: 520px;
    background: linear-gradient(90deg, rgba(11,109,181,0) 0%, rgba(58,79,112,0.75) 35%, #50627e 65%, #7a3a3a 80%, #4b5f80 100%);
  }
  .banner--skids .photo {
    left: 0; width: 360px;
    background: linear-gradient(90deg, #0d4f92 0%, #2f7fc0 40%, #5d95c8 70%, #2a5d9a 100%);
  }
  .banner--tanks .photo {
    left: 0; width: 460px;
    background: linear-gradient(90deg, var(--steel-dark) 0%, var(--steel) 35%, rgba(27,61,120,0.6) 70%, var(--navy) 100%);
  }

  .label-box {
    position: absolute; left: 66px; top: 29px;
    width: 356px; height: 35px;
    border: 1.5px solid var(--white);
    color: var(--white);
    font-weight: 500; font-size: 20px; letter-spacing: 0.2px;
    display: flex; align-items: center; justify-content: center;
  }
  .headline {
    position: absolute;
    font-family: "Oswald", "Arial Narrow", sans-serif;
    font-weight: 600;
    color: var(--white);
    text-transform: uppercase;
    white-space: nowrap;
  }
  .banner--spools .headline { left: 66px; top: 78px; font-size: 29px; }

  .subtitle {
    position: absolute;
    color: var(--sky);
    font-weight: 400;
    font-size: 21px;
    white-space: nowrap;
  }
  .banner--skids .subtitle { right: 69px; top: 30px; }
  .banner--skids .headline { right: 69px; top: 70px; font-size: 35px; }

  .banner--tanks .text-block {
    position: absolute; left: 270px; width: 480px; top: 0; height: 100%;
    text-align: center;
  }
  .banner--tanks .subtitle { left: 0; right: 0; top: 30px; }
  .banner--tanks .headline { left: 0; right: 0; top: 70px; font-size: 35px; }

  .chevron { position: absolute; left: 0; top: 0; }
  .tank-visual {
    position: absolute; left: 790px; top: 18px;
    width: 182px; height: 128px;
    border-radius: 91px 91px 0 0;
    background: linear-gradient(180deg, #f2f4f7 0%, #c9cfd8 100%);
  }
</style>
</head>
<body>
  <section class="banner banner--spools">
    <div class="photo" role="img" aria-label="Stacks of steel process pipes in a fabrication yard"></div>
    <div class="label-box">PIPING SPOOLS FABRICATION</div>
    <h2 class="headline">Expert Fabrication Solutions for Process Piping</h2>
  </section>

  <section class="banner banner--skids">
    <div class="photo" role="img" aria-label="Blue-toned industrial skid and frame structure"></div>
    <svg class="chevron" width="460" height="146" viewBox="0 0 460 146" aria-hidden="true">
      <polygon points="375,0 460,0 460,0 345,73 460,146 375,146 300,73" fill="var(--sky-soft)"/>
      <polygon points="398,0 460,0 460,0 370,73 460,146 398,146 325,73" fill="var(--navy)"/>
      <rect x="430" y="0" width="30" height="146" fill="var(--navy)"/>
    </svg>
    <div class="subtitle">SKID &amp; FRAMES FABRICATION</div>
    <h2 class="headline">Custom Engineered Modular Systems</h2>
  </section>

  <section class="banner banner--tanks">
    <div class="photo" role="img" aria-label="Steel pipework and fittings in a workshop"></div>
    <svg class="chevron" width="1022" height="146" viewBox="0 0 1022 146" aria-hidden="true">
      <polygon points="750,0 1006,0 970,40 786,40" fill="var(--sky-soft)"/>
    </svg>
    <div class="tank-visual" role="img" aria-label="Fabricated small steel tank with top-mounted mixer"></div>
    <div class="text-block">
      <div class="subtitle">SMALL STEEL TANKS FABRICATION</div>
      <h2 class="headline">Precision Built for Your Needs</h2>
    </div>
  </section>
</body>
</html>
```